Allies for Wellness Resources- Medical Billing and Consultant Firm Business card

We need a logo design for a medical billing and healthcare consulting firm. We help physician medical practices achieve their financial objectives by providing medical billing services and other revenue cycle services. We want a business card design that is eye catching and compliments the color and design my logo. We like variations of blue colors however we are very open to other colors. We would like the services we provide listed on the back of the card.

Target Market(s)

Doctors and medical practices

Industry/Entity Type

Medical

Contact Information for Business Card

Space for logo, name, title, phone #, address, web address

Font styles to use
Serif
Sans Serif

Colors

Designer to choose colors to be used in the design.

Requirements
Must have
• Company Services listed on the back.
Should not have
• We are pretty open to all design ideas

```html
<!DOCTYPE html>
<html lang="en">
<head>
<meta charset="utf-8">
<title>Allies for Wellness Resources – Business Card</title>
<link rel="stylesheet" href="https://fonts.googleapis.com/css2?family=Cinzel:wght@600&family=Montserrat:wght@400;500&display=swap">
<style>
  :root {
    --bg: #2b2c2e;
    --brand-blue: #1158a8;
    --accent-blue: #3a9ad9;
    --paper: #ffffff;
    --ink-light: #ffffff;
  }
  * { box-sizing: border-box; margin: 0; padding: 0; }
  html, body { width: 1200px; height: 880px; overflow: hidden; background: var(--bg); }
  .canvas { position: relative; width: 1200px; height: 880px; }

  .card {
    position: absolute;
    width: 640px;
    height: 366px;
    border-radius: 22px;
    overflow: hidden;
    box-shadow: 0 14px 30px rgba(0,0,0,0.45);
  }
  .card-back { left: 70px; top: 70px; background: var(--brand-blue); }
  .card-front { left: 490px; top: 470px; background: var(--brand-blue); }

  /* Wordmark */
  .wordmark {
    display: flex;
    align-items: center;
    gap: 14px;
    font-family: 'Cinzel', Georgia, serif;
    font-weight: 600;
    letter-spacing: 0.06em;
    line-height: 1.2;
  }
  .wordmark-dot { width: 22px; height: 22px; border-radius: 50%; flex: none; }
  .wordmark-name { font-size: 25px; }

  .card-back .wordmark { position: absolute; left: 0; right: 0; top: 96px; justify-content: center; color: var(--ink-light); }
  .card-back .wordmark-dot { background: var(--ink-light); }

  .services {
    position: absolute;
    left: 0; right: 0; top: 236px;
    text-align: center;
    font-family: 'Montserrat', Arial, sans-serif;
    font-weight: 400;
    font-size: 14px;
    line-height: 1.7;
    color: var(--ink-light);
    letter-spacing: 0.01em;
  }

  /* Front */
  .front-shape { position: absolute; inset: 0; width: 640px; height: 366px; }
  .front-shape .paper { fill: var(--paper); }
  .front-shape .swoosh { fill: none; stroke: var(--accent-blue); stroke-width: 4; }

  .card-front .wordmark { position: absolute; left: 338px; top: 118px; color: var(--brand-blue); }
  .card-front .wordmark-dot { background: var(--brand-blue); }
  .card-front .wordmark-name { font-size: 21px; }

  .holder { position: absolute; left: 42px; top: 48px; color: var(--ink-light); font-family: 'Montserrat', Arial, sans-serif; }
  .holder-name { font-size: 22px; font-weight: 500; letter-spacing: 0.02em; }
  .holder-title { font-size: 15px; font-weight: 400; }

  .address {
    position: absolute; left: 42px; top: 160px;
    font-family: 'Montserrat', Arial, sans-serif; font-size: 15px; line-height: 1.45;
    color: var(--ink-light);
  }
  .contacts {
    position: absolute; left: 42px; top: 232px; list-style: none;
    font-family: 'Montserrat', Arial, sans-serif; font-size: 15px;
    color: var(--ink-light);
  }
  .contacts li { display: flex; align-items: center; gap: 10px; height: 27px; }
  .contact-icon { width: 20px; height: 20px; flex: none; }
  .contact-icon circle.ring { fill: none; stroke: var(--ink-light); stroke-width: 1.4; }
  .contact-icon .glyph { fill: none; stroke: var(--ink-light); stroke-width: 1.3; stroke-linecap: round; stroke-linejoin: round; }
</style>
</head>
<body>
<main class="canvas">

  <section class="card card-back" aria-label="Card back">
    <div class="wordmark">
      <span class="wordmark-dot"></span>
      <span class="wordmark-name">Allies for Wellness<br>Resources LLC</span>
    </div>
    <p class="services">
      Local Community Marketing | Word-of-Mouth Marketing | B2B Marketing<br>
      Special Projects and Event Marketing
    </p>
  </section>

  <section class="card card-front" aria-label="Card front">
    <svg class="front-shape" viewBox="0 0 640 366" aria-hidden="true">
      <path class="paper" d="M258 0 Q300 250 470 366 L640 366 L640 0 Z"/>
      <path class="swoosh" d="M246 0 Q288 258 456 366"/>
    </svg>

    <div class="wordmark">
      <span class="wordmark-dot"></span>
      <span class="wordmark-name">Allies for<br>Wellness<br>Resources LLC</span>
    </div>

    <div class="holder">
      <p class="holder-name">JORDAN HALE</p>
      <p class="holder-title">Owner</p>
    </div>

    <p class="address">PO BOX 481 Harbor Lane<br>7th street Ashford</p>

    <ul class="contacts">
      <li>
        <svg class="contact-icon" viewBox="0 0 20 20" aria-hidden="true">
          <circle class="ring" cx="10" cy="10" r="9"/>
          <path class="glyph" d="M7 5.5 L8.6 7.6 L7.8 8.8 Q8.8 11 11.2 12.2 L12.4 11.4 L14.5 13 L13.4 14.4 Q9.5 14.2 6.2 9.6 Q5.7 6.8 7 5.5 Z"/>
        </svg>
        <span>(555) 210-4836</span>
      </li>
      <li>
        <svg class="contact-icon" viewBox="0 0 20 20" aria-hidden="true">
          <circle class="ring" cx="10" cy="10" r="9"/>
          <rect class="glyph" x="5" y="6.5" width="10" height="7" rx="0.8"/>
          <path class="glyph" d="M5.3 7 L10 10.6 L14.7 7"/>
        </svg>
        <span>hello@allieswellness.com</span>
      </li>
      <li>
        <svg class="contact-icon" viewBox="0 0 20 20" aria-hidden="true">
          <circle class="ring" cx="10" cy="10" r="9"/>
          <circle class="glyph" cx="10" cy="10" r="5"/>
          <ellipse class="glyph" cx="10" cy="10" rx="2.2" ry="5"/>
          <path class="glyph" d="M5 10 H15"/>
        </svg>
        <span>www.allieswellness.com</span>
      </li>
    </ul>
  </section>

</main>
</body>
</html>
```